Flyer for the Radiant Harvest Worship Day 2020

I am looking to create a flyer for a one day prayer retreat our church is organizing.
This flyer will be posted on social media, websites and will also be printed so it can be mailed to people.
I am looking for something professional, with good use of our logo and band colors (logo colors).
I am counting on the designer's skill, creativity, art and knowledge of media communication to produce a flyer that will effectively and quickly convey the message we are trying to spread.
CONTENT OF THE FLYER:
Event title: Radiant Harvest Worship Day
Date: Tuesday July 2nd, 2020
Time: 11:00AM - 7:00PM
Maplewood Hotel, 4817 Birchfield Avenue, Portland, Maine 04109 (Room: Evergreen)
Event Key words to highlight what the event is about: Prayer, Sharing the Word, Panel discussion, prophecy, Impartation.
Key phrases:
A one day prayer retreat.
Jesus Chris is Lord
Contact info:
www.tolvex.org
Phone: 207 555 0143
Email: contact@brookmeadow.org

```html
<!DOCTYPE html>
<html lang="en">
<head>
<meta charset="utf-8">
<title>Radiant Harvest Worship Day 2020</title>
<link href="https://fonts.googleapis.com/css2?family=Cinzel:wght@400;500&family=Montserrat:ital,wght@0,400;0,500;0,700;1,400&family=Playfair+Display:ital,wght@1,900&display=swap" rel="stylesheet">
<style>
  :root {
    --page: #ffffff;
    --navy: #0b3960;
    --navy-deep: #07304f;
    --orange: #f7941d;
    --white: #ffffff;
    --rule: rgba(255,255,255,0.55);
    --photo-warm: #b9825f;
    --photo-light: #e9d6c4;
  }
  * { margin: 0; padding: 0; box-sizing: border-box; }
  html, body { width: 1200px; height: 1200px; overflow: hidden; background: var(--page); }
  .flyer {
    position: absolute; left: 185px; top: 63px; width: 830px; height: 1074px;
    background: var(--navy); color: var(--white); overflow: hidden;
    font-family: "Montserrat", sans-serif;
  }
  .hero-photo {
    position: absolute; left: 0; top: 0; width: 100%; height: 430px;
    background:
      radial-gradient(ellipse at 55% 10%, var(--photo-light) 0%, rgba(233,214,196,0) 45%),
      radial-gradient(ellipse at 20% 30%, var(--photo-warm) 0%, rgba(185,130,95,0) 40%),
      radial-gradient(ellipse at 80% 35%, #c89a7e 0%, rgba(200,154,126,0) 40%),
      linear-gradient(180deg, #8a6a5a 0%, #5d5f6e 45%, var(--navy) 100%);
  }
  .hero-fade {
    position: absolute; left: 0; top: 240px; width: 100%; height: 200px;
    background: linear-gradient(180deg, rgba(11,57,96,0) 0%, var(--navy) 90%);
  }
  .brand {
    position: absolute; top: 288px; left: 0; width: 100%;
    display: flex; justify-content: center; align-items: center; gap: 12px;
  }
  .brand-dot { width: 18px; height: 18px; border-radius: 50%; background: var(--orange); }
  .brand-name { font-family: "Cinzel", serif; font-weight: 400; font-size: 58px; letter-spacing: 1px; color: var(--white); }
  .divider-row {
    position: absolute; left: 0; width: 100%;
    display: flex; align-items: center; justify-content: center; gap: 26px;
  }
  .divider-row .rule { height: 2px; background: var(--rule); }
  .present { top: 382px; }
  .present .label { font-style: italic; font-size: 25px; letter-spacing: 4px; }
  .dove {
    position: absolute; left: 607px; top: 386px; width: 84px; height: 96px;
    background: radial-gradient(circle at 50% 50%, #ffffff 0%, #dfe8f2 35%, rgba(223,232,242,0) 70%);
  }
  .title-script {
    position: absolute; top: 422px; left: 0; width: 100%; text-align: center;
    font-family: "Playfair Display", serif; font-style: italic; font-weight: 900;
    font-size: 92px; color: var(--orange); padding-left: 20px;
  }
  .title-main {
    position: absolute; top: 526px; left: 0; width: 100%; text-align: center;
    font-family: "Cinzel", serif; font-weight: 400; font-size: 108px; line-height: 1; letter-spacing: 2px;
  }
  .title-sub {
    position: absolute; top: 642px; left: 0; width: 100%; text-align: center;
    font-size: 46px; font-weight: 400; letter-spacing: 10px; padding-left: 10px;
  }
  .tagline {
    position: absolute; top: 700px; left: 0; width: 100%; text-align: center;
    font-size: 11px; font-weight: 700; letter-spacing: 13px; padding-left: 13px;
  }
  .featuring { top: 732px; }
  .featuring .label { font-style: italic; font-size: 27px; letter-spacing: 1px; }
  .keywords {
    position: absolute; top: 774px; left: 0; width: 100%; text-align: center;
    font-family: "Cinzel", serif; font-size: 21px; line-height: 29px; letter-spacing: 1px;
  }
  .info-rule { position: absolute; top: 842px; left: 135px; width: 560px; height: 1px; background: rgba(255,255,255,0.3); }
  .info { position: absolute; top: 860px; left: 0; width: 100%; height: 100px; }
  .info .col { position: absolute; top: 0; text-align: center; }
  .info .head { display: flex; align-items: center; justify-content: center; gap: 4px; font-size: 19px; }
  .info .head svg { width: 17px; height: 17px; }
  .info .divider { position: absolute; top: 18px; width: 2px; height: 74px; background: var(--rule); }
  .col-date { left: 129px; width: 140px; }
  .date-day { font-size: 25px; font-weight: 700; margin-top: 8px; line-height: 1; }
  .date-year { font-size: 40px; font-weight: 400; line-height: 1.1; }
  .col-venue { left: 290px; width: 300px; font-size: 18px; line-height: 25px; }
  .col-venue .head { margin-bottom: 3px; }
  .col-venue strong { font-weight: 700; }
  .col-time { left: 610px; width: 130px; }
  .time { display: flex; align-items: center; justify-content: center; margin-top: 8px; font-weight: 700; font-size: 36px; line-height: 1; }
  .time .unit { display: flex; flex-direction: column; font-size: 12px; font-weight: 500; line-height: 12px; margin: 0 2px; }
  .contact {
    position: absolute; top: 983px; left: 0; width: 100%; text-align: center;
    font-size: 15.5px; font-weight: 500; letter-spacing: 1px;
  }
  .closing {
    position: absolute; top: 1022px; left: 0; width: 100%; text-align: center;
    font-family: "Cinzel", serif; font-size: 24px; letter-spacing: 1px;
  }
</style>
</head>
<body>
  <main class="flyer">
    <div class="hero-photo" role="img" aria-label="Photograph of a group holding hands around a table in prayer"></div>
    <div class="hero-fade"></div>

    <div class="brand">
      <span class="brand-dot"></span>
      <span class="brand-name">TOLVEX</span>
    </div>

    <div class="divider-row present">
      <span class="rule" style="width:165px"></span>
      <span class="label">present</span>
      <span class="rule" style="width:165px"></span>
    </div>
    <div class="dove" role="img" aria-label="Illustration of a white dove in flight with a soft glow"></div>

    <h1>
      <span class="title-script">Radiant</span>
      <span class="title-main">HARVEST</span>
      <span class="title-sub">WORSHIP DAY</span>
    </h1>
    <p class="tagline">A ONE DAY PRAYER RETREAT</p>

    <div class="divider-row featuring">
      <span class="rule" style="width:300px"></span>
      <span class="label">featuring</span>
      <span class="rule" style="width:290px"></span>
    </div>
    <p class="keywords">
      PRAYER | SHARING THE WORD<br>
      PANEL DISCUSSION | PROPHECY | IMPARTATION.
    </p>

    <div class="info-rule"></div>
    <section class="info">
      <div class="col col-date">
        <div class="head">
          <svg viewBox="0 0 16 16" fill="none" stroke="#f7941d" stroke-width="1.5"><rect x="1.5" y="3" width="13" height="11.5" rx="1"/><line x1="1.5" y1="6.5" x2="14.5" y2="6.5"/><line x1="5" y1="1" x2="5" y2="4"/><line x1="11" y1="1" x2="11" y2="4"/></svg>
          DATE
        </div>
        <div class="date-day">02,JULY</div>
        <div class="date-year">2020</div>
      </div>
      <span class="divider" style="left:278px"></span>
      <div class="col col-venue">
        <div class="head">
          <svg viewBox="0 0 16 16" fill="none" stroke="#f7941d" stroke-width="1.5"><path d="M8 15s5-5 5-9A5 5 0 0 0 3 6c0 4 5 9 5 9z"/><circle cx="8" cy="6" r="2"/></svg>
          VENUE
        </div>
        <div><strong>Maplewood Hotel</strong>, 4817 Birchfield</div>
        <div>Avenue, Portland, Maine 04109</div>
        <div>(Room: Evergreen)</div>
      </div>
      <span class="divider" style="left:597px"></span>
      <div class="col col-time">
        <div class="head">
          <svg viewBox="0 0 16 16" fill="none" stroke="#f7941d" stroke-width="1.5"><circle cx="8" cy="8" r="6.5"/><polyline points="5,8 7.3,10.3 11,6"/></svg>
          TIME
        </div>
        <div class="time">11<span class="unit"><span>:00</span><span>AM</span></span>-7<span class="unit"><span>:00</span><span>PM</span></span></div>
      </div>
    </section>

    <p class="contact">www.tolvex.org | Phone: 207 555 0143 |Email:contact@brookmeadow.org</p>
    <p class="closing">Jesus Chris is Lord</p>
  </main>
</body>
</html>
```